Local Finance and Insurance Advising Company from Switzerland needs an impressive banner design.

I am looking for an impressive Banner Design, I need this Banner for Facebook, LinkedIn, YouTube & Google.

I am Advising all kind of peoples who are living here in Switzerland. Young, middle age and old people. People who want to go study, people who are planning to create a family, old people who are, or going to retire. Expatriates who want to leave Switzerland to live in another country, expatriates who are coming to Switzerland. Peoples who ant to build their own business up. All kind of financial, insurance and pension planning's.

The Company Name is: Alpine Counsel
Our slogen / heading is: Clear Guidance, no Pitch

The Company logo can be used for the banner, but I would preffer to have the banner without logo, as the logo will be already in a another field on the social networks.

Since the first impression is the most important, this project is really important to me. I am ready to realize further projects with the one who can create the perfect banner who hits the point as described. I am a start-up company, everything is still on beginning and still much has to be done.

Target Market(s)

private clients

Requirements
Must have
• The banner should give the impression of happiness, safeness, health and freedom. Empowering people and creating freedom lifestyles.
Should not have
• I do not want that the banner looks like we are some kind of broker who is just selling some kind of insurances.

```html
<!DOCTYPE html>
<html lang="en">
<head>
<meta charset="utf-8">
<title>Alpine Counsel – Clear Guidance, no Pitch</title>
<link rel="stylesheet" href="https://fonts.googleapis.com/css2?family=Poppins:wght@700;800&display=swap">
<style>
  :root {
    --brand-red: #e3262c;
    --brand-red-deep: #c41d23;
    --brand-red-soft: #d9444a;
    --divider-white: #ffffff;
    --sky-light: #f3f1ea;
    --autumn-gold: #e0a24a;
    --autumn-orange: #cf7a34;
    --stone-warm: #c49a72;
    --scarf-red: #b8323a;
    --coat-navy: #2c3650;
    --photo-grey: #8e9290;
    --photo-grey-dark: #6f7472;
    --headline-white: #ffffff;
  }
  html, body {
    margin: 0;
    padding: 0;
    overflow: hidden;
    background: #ffffff;
  }
  .banner {
    position: relative;
    width: 1200px;
    height: 457px;
    overflow: hidden;
    font-family: "Poppins", sans-serif;
  }
  .banner-shapes {
    position: absolute;
    inset: 0;
    display: block;
  }
  .headline {
    position: absolute;
    inset: 0;
    margin: 0;
    color: var(--headline-white);
    font-weight: 800;
    text-transform: uppercase;
    line-height: 1;
  }
  .headline-line {
    position: absolute;
    display: block;
    white-space: nowrap;
    letter-spacing: 0.5px;
  }
  .line-clear { left: 757px; top: 46px; font-size: 104px; }
  .line-guidance { left: 712px; top: 158px; font-size: 66px; font-weight: 700; }
  .line-no { left: 685px; top: 250px; font-size: 88px; }
  .line-pitch { left: 644px; top: 348px; font-size: 67px; font-weight: 700; }
</style>
</head>
<body>
  <main class="banner">
    <svg class="banner-shapes" width="1200" height="457" viewBox="0 0 1200 457" xmlns="http://www.w3.org/2000/svg">
      <defs>
        <linearGradient id="tint-left" x1="0" y1="0" x2="1" y2="1">
          <stop offset="0" stop-color="var(--brand-red-deep)"/>
          <stop offset="1" stop-color="var(--brand-red-soft)"/>
        </linearGradient>
        <linearGradient id="photo-base" x1="0" y1="0" x2="0.9" y2="1">
          <stop offset="0" stop-color="var(--autumn-orange)"/>
          <stop offset="0.35" stop-color="var(--stone-warm)"/>
          <stop offset="0.7" stop-color="var(--autumn-gold)"/>
          <stop offset="1" stop-color="var(--coat-navy)"/>
        </linearGradient>
        <radialGradient id="photo-sunlight" cx="0.62" cy="0.12" r="0.45">
          <stop offset="0" stop-color="var(--sky-light)" stop-opacity="0.95"/>
          <stop offset="1" stop-color="var(--sky-light)" stop-opacity="0"/>
        </radialGradient>
        <radialGradient id="photo-warmth" cx="0.3" cy="0.8" r="0.35">
          <stop offset="0" stop-color="var(--scarf-red)" stop-opacity="0.55"/>
          <stop offset="1" stop-color="var(--scarf-red)" stop-opacity="0"/>
        </radialGradient>
        <linearGradient id="tint-center" x1="0" y1="0" x2="1" y2="1">
          <stop offset="0" stop-color="var(--brand-red)"/>
          <stop offset="1" stop-color="var(--brand-red-deep)"/>
        </linearGradient>
        <linearGradient id="tint-right" x1="0" y1="0" x2="0" y2="1">
          <stop offset="0" stop-color="var(--photo-grey)"/>
          <stop offset="1" stop-color="var(--photo-grey-dark)"/>
        </linearGradient>
      </defs>

      <polygon class="panel panel--left" points="0,0 187,0 66,457 0,457" fill="url(#tint-left)"
               role="img" aria-label="Red-tinted photo of autumn trees"/>
      <g class="panel panel--couple" role="img"
         aria-label="Photo of a smiling retired couple laughing together at a swing in front of an old stone house on a sunny autumn day">
        <polygon points="187,0 717,0 520,457 66,457" fill="url(#photo-base)"/>
        <polygon points="187,0 717,0 520,457 66,457" fill="url(#photo-sunlight)"/>
        <polygon points="187,0 717,0 520,457 66,457" fill="url(#photo-warmth)"/>
      </g>
      <polygon class="panel panel--headline" points="717,0 1156,0 1010,457 520,457" fill="url(#tint-center)"
               role="img" aria-label="Red-tinted photo of a river and waterfall"/>
      <polygon class="panel panel--right" points="1156,0 1200,0 1200,457 1010,457" fill="url(#tint-right)"
               role="img" aria-label="Grey-toned photo of a riverside landscape"/>

      <g class="dividers" stroke="var(--divider-white)" stroke-width="8">
        <line x1="189" y1="-4" x2="64" y2="461"/>
        <line x1="719" y1="-4" x2="518" y2="461"/>
        <line x1="1158" y1="-4" x2="1008" y2="461"/>
      </g>
    </svg>

    <h1 class="headline" aria-label="Clear Guidance, no Pitch">
      <span class="headline-line line-clear">Clear</span>
      <span class="headline-line line-guidance">Guidance</span>
      <span class="headline-line line-no">No</span>
      <span class="headline-line line-pitch">Pitch</span>
    </h1>
  </main>
</body>
</html>
```